Business Card Design

Please use the Logo for colors and styles, and create a business card using the following info:

Matthias Lorbeer
Web Developer

Lorbeer Systems
+41 76 418 57 90
matthias@lorbeer-systems.ch
www.lorbeer-systems.ch

Download the logo at http://lorbeer-systems.ch/tl_files/lorbeer_systems.zip

Thanks for your works!

```html
<!DOCTYPE html>
<html lang="en">
<head>
<meta charset="utf-8">
<title>Lorbeer Systems – Business Card</title>
<link rel="stylesheet" href="https://fonts.googleapis.com/css2?family=Arimo:wght@400&display=swap">
<style>
  :root {
    --page-bg: #ffffff;
    --card-frame: #262c2c;
    --panel: #ffffff;
    --ink: #34344f;
    --logo-band: #1c1c1c;
    --logo-ink: #ffffff;
    --keys-light: #d3dddc;
    --keys-mid: #9fb0ae;
    --keys-dark: #2a3030;
  }
  * { margin: 0; padding: 0; box-sizing: border-box; }
  html, body {
    width: 761px;
    height: 1200px;
    overflow: hidden;
    background: var(--page-bg);
  }
  .card {
    position: absolute;
    left: 37px;
    top: 37px;
    width: 684px;
    height: 1124px;
    background: var(--card-frame);
    font-family: "Arimo", Arial, sans-serif;
    color: var(--ink);
    overflow: hidden;
  }
  .contact-panel {
    position: absolute;
    left: 43px;
    top: 54px;
    width: 596px;
    height: 646px;
    background: var(--panel);
    border-radius: 9px;
    text-align: center;
  }
  .contact-panel > * {
    position: absolute;
    left: 0;
    right: 0;
    line-height: 1;
  }
  .person-name {
    top: 103px;
    font-size: 43px;
    font-weight: 400;
    text-transform: uppercase;
    letter-spacing: 1px;
  }
  .job-title {
    top: 200px;
    font-size: 37px;
    font-variant: small-caps;
    letter-spacing: 1.5px;
  }
  .phone {
    top: 318px;
    font-size: 40px;
    letter-spacing: 0.5px;
  }
  .email {
    top: 447px;
    font-size: 33px;
  }
  .website {
    top: 546px;
    font-size: 28px;
    text-transform: uppercase;
    letter-spacing: 2px;
  }
  .logo-band {
    position: absolute;
    left: 0;
    top: 700px;
    width: 100%;
    height: 159px;
    background: var(--logo-band);
    display: flex;
    align-items: center;
    justify-content: center;
  }
  .company-name {
    font-size: 50px;
    color: var(--logo-ink);
    text-transform: uppercase;
    letter-spacing: 1px;
    font-weight: 400;
  }
  .keyboard-art {
    position: absolute;
    left: 0;
    top: 859px;
    width: 100%;
    height: 265px;
    background: linear-gradient(180deg, var(--keys-mid) 0%, var(--keys-light) 45%, var(--keys-mid) 100%);
  }
</style>
</head>
<body>
  <div class="card">
    <section class="contact-panel">
      <h1 class="person-name">Matthias Lorbeer</h1>
      <p class="job-title">Web Developer</p>
      <p class="phone">+41 76 418 57 90</p>
      <p class="email">matthias@lorbeer-systems.ch</p>
      <p class="website">www.lorbeer-systems.ch</p>
    </section>
    <div class="logo-band">
      <span class="company-name">Lorbeer Systems</span>
    </div>
    <div class="keyboard-art" role="img" aria-label="Illustration of light grey computer keyboard keys"></div>
  </div>
</body>
</html>
```